Business Card for Multi-Brand Sportswear Company

We are looking for a business card which represents our company and the multiple brands within it.

The company: Kelvo Athletics (LTD)
The brands: Kelv, TaliMati, VerdantFlex, Grit and Grime

Employees using these cards would be representing Kelvo Athletics, rather than any of the individual brands. You will see a current design within the uploaded files, to give some inspiration. The actual text of the brands is not necessary, but the logos should be on there is some format.

Our creative minds on this are stretched, so we are looking for someone to make this their own, and show us what a good business card should look like.

We may like to get these printed with spot gloss, so keep that in mind with your designs.

www.kelvoathletics.co.uk

Industry/Entity Type

Business

Contact Information for Business Card

Tom Pennington-Hale
Operations Manager
(+44) 1632 960 417
Tom@kelvoathletics.co.uk
www.kelvoathletics.co.uk

Font styles to use
Sans Serif
Other font styles liked:
• Eurostile

Colors
ffffff

Requirements
Nice to have
• Dark (black) background

```html
<!DOCTYPE html>
<html lang="en">
<head>
<meta charset="utf-8">
<title>Kelvo Athletics – Business Card</title>
<link rel="stylesheet" href="https://fonts.googleapis.com/css2?family=Quicksand:wght@400;500;600&display=swap">
<style>
  :root {
    --backdrop: #8f8f8f;
    --card: #2d2c2b;
    --card-shadow: rgba(0, 0, 0, 0.35);
    --band-top: #3a3938;
    --band-bottom: #1c1b1b;
    --band-edge: #111010;
    --text: #ffffff;
    --muted: #d9d9d9;
    --accent: #e3272a;
    --gloss: #1c1b1b;
  }
  * { box-sizing: border-box; margin: 0; padding: 0; }
  html, body {
    width: 1200px; height: 854px; overflow: hidden;
    background: var(--backdrop);
    font-family: "Quicksand", sans-serif;
    color: var(--text);
  }
  .canvas { position: relative; width: 1200px; height: 854px; }
  .card {
    position: absolute; top: 281px;
    width: 512px; height: 293px;
    background: var(--card);
    box-shadow: 0 6px 24px var(--card-shadow);
  }
  .card--front { left: 78px; }
  .card--back { left: 609px; }

  .logo-band { position: absolute; left: 0; top: 98px; width: 284px; height: 62px; }
  .logo-band svg { position: absolute; inset: 0; }
  .wordmark {
    position: absolute; left: 34px; top: 0; height: 60px;
    display: flex; align-items: center; gap: 8px;
    font-weight: 600; font-size: 19px; letter-spacing: 0.5px;
    color: var(--text); white-space: nowrap;
  }
  .wordmark__dot { width: 9px; height: 9px; border-radius: 50%; background: var(--accent); }

  .contact { position: absolute; right: 28px; text-align: right; white-space: nowrap; }
  .contact__name { top: 114px; font-size: 19px; font-weight: 600; }
  .contact__role { top: 146px; font-size: 15px; font-weight: 500; }
  .contact__details { top: 195px; font-size: 14px; font-weight: 500; line-height: 24px; }

  .brand-row {
    position: absolute; display: flex; align-items: center;
    gap: 9px; white-space: nowrap; color: var(--muted); font-weight: 600;
  }
  .card--front .brand-row { left: 44px; top: 242px; font-size: 9px; }
  .card--back .brand-row { left: 50%; transform: translateX(-50%); top: 236px; font-size: 12px; gap: 14px; }
  .brand-row__item { display: flex; align-items: center; gap: 4px; }
  .brand-row__mark { width: 6px; height: 6px; border-radius: 50%; background: var(--accent); }

  .gloss-mark {
    position: absolute; left: 0; right: 0; top: 92px;
    text-align: center; font-size: 46px; font-weight: 600;
    letter-spacing: 1px; color: var(--gloss); white-space: nowrap;
    display: flex; justify-content: center; align-items: center; gap: 14px;
  }
  .gloss-mark__dot { width: 16px; height: 16px; border-radius: 50%; background: var(--accent); }
</style>
</head>
<body>
<div class="canvas">

  <section class="card card--front" aria-label="Business card front">
    <div class="logo-band">
      <svg width="284" height="62" viewBox="0 0 284 62">
        <defs>
          <linearGradient id="bandFill" x1="0" y1="0" x2="0" y2="1">
            <stop offset="0" stop-color="var(--band-top)"/>
            <stop offset="1" stop-color="var(--band-bottom)"/>
          </linearGradient>
        </defs>
        <polygon points="1,1 282,1 226,60 1,60" fill="url(#bandFill)" stroke="var(--band-edge)" stroke-width="2"/>
      </svg>
      <div class="wordmark"><span>Kelvo Athletics</span><span class="wordmark__dot"></span></div>
    </div>

    <p class="contact contact__name">Tom Pennington-Hale</p>
    <p class="contact contact__role">Operations Manager</p>
    <div class="contact contact__details">
      <p>(+44) 1632 960 417</p>
      <p>Tom@kelvoathletics.co.uk</p>
      <p>www.kelvoathletics.co.uk</p>
    </div>

    <div class="brand-row">
      <span class="brand-row__item">VerdantFlex</span>
      <span class="brand-row__item"><span class="brand-row__mark"></span>Grit and Grime</span>
      <span class="brand-row__item">Kelv</span>
      <span class="brand-row__item">TaliMati</span>
    </div>
  </section>

  <section class="card card--back" aria-label="Business card back">
    <div class="gloss-mark"><span>Kelvo Athletics</span><span class="gloss-mark__dot"></span></div>
    <div class="brand-row">
      <span class="brand-row__item">VerdantFlex</span>
      <span class="brand-row__item"><span class="brand-row__mark"></span>Grit and Grime</span>
      <span class="brand-row__item">Kelv</span>
      <span class="brand-row__item">TaliMati</span>
    </div>
  </section>

</div>
</body>
</html>
```